Criação de Folder para Alimentos & Bebidas
A empresa queria:
" importamos produtos com nossas marcas e distribuimos para supermercdos e distribuidores "

```html
<!DOCTYPE html>
<html lang="pt-BR">
<head>
<meta charset="UTF-8">
<title>Folder Alimentos &amp; Bebidas</title>
<link href="https://fonts.googleapis.com/css2?family=Quicksand:wght@500;600;700&display=swap" rel="stylesheet">
<style>
  :root {
    --backdrop: #ecebea;
    --paper: #ffffff;
    --ink-dark: #141212;
    --gold-deep: #9c6a12;
    --gold: #d9a431;
    --gold-light: #f4d27a;
    --caption-gold: #e6b54c;
    --text-light: #f3efe9;
  }
  * { box-sizing: border-box; margin: 0; padding: 0; }
  html, body {
    width: 1200px; height: 1200px; overflow: hidden;
    background: var(--backdrop);
    font-family: "Quicksand", sans-serif;
  }
  .spread {
    position: absolute; left: 50px; top: 160px;
    width: 1100px; height: 880px;
    display: flex;
    box-shadow: 0 18px 40px rgba(0,0,0,0.18);
  }
  .page {
    position: relative; width: 550px; height: 880px;
    background: var(--paper); overflow: hidden;
  }
  .page-art { position: absolute; inset: 0; width: 550px; height: 880px; }
  .fold-shade { position: absolute; top: 0; bottom: 0; width: 40px; pointer-events: none; }
  .page--about .fold-shade { right: 0; background: linear-gradient(to left, rgba(0,0,0,0.12), rgba(0,0,0,0)); }
  .page--products .fold-shade { left: 0; background: linear-gradient(to right, rgba(0,0,0,0.12), rgba(0,0,0,0)); }
  .section-title {
    position: absolute; top: 62px; left: 50%; transform: translateX(-50%);
    width: 320px; height: 46px; border-radius: 23px;
    background: var(--ink-dark); color: var(--gold-light);
    font-weight: 600; font-size: 20px; letter-spacing: 0.3px;
    display: flex; align-items: center; justify-content: center;
  }
  .about-text {
    position: absolute; left: 42px; top: 400px; width: 455px;
    color: var(--text-light); font-size: 14.5px; line-height: 1.42; font-weight: 600;
  }
  .about-text p + p { margin-top: 18px; }
  .product-grid {
    position: absolute; left: 60px; top: 350px; width: 440px;
    display: grid; grid-template-columns: 1fr 1fr; row-gap: 30px; column-gap: 20px;
  }
  .product { display: flex; flex-direction: column; align-items: center; }
  .product-photo {
    width: 140px; height: 135px; border: 5px solid var(--gold);
    border-radius: 5px; box-shadow: 0 0 0 1px var(--gold-deep);
  }
  .product-photo--lamb { background: linear-gradient(135deg, #e9c3b8, #b9534a 60%, #5a2a22); }
  .product-photo--beef { background: linear-gradient(135deg, #d96a66, #a8282c 55%, #5c1a1a); }
  .product-photo--fish { background: linear-gradient(135deg, #c9d3d6, #8a9aa1 55%, #3d5160); }
  .product-photo--fries { background: linear-gradient(135deg, #f6d35c, #e79a24 60%, #7a3f12); }
  .product-name {
    margin-top: 12px; text-align: center; color: var(--caption-gold);
    font-weight: 700; font-size: 17px; line-height: 1.25; white-space: nowrap;
  }
</style>
</head>
<body>
  <div class="spread">
    <section class="page page--about">
      <svg class="page-art" viewBox="0 0 550 880">
        <defs>
          <linearGradient id="goldBandLeft" x1="0" y1="0" x2="1" y2="0">
            <stop offset="0" stop-color="#9c6a12"/>
            <stop offset="0.6" stop-color="#d9a431"/>
            <stop offset="1" stop-color="#f4d27a"/>
          </linearGradient>
          <linearGradient id="meatPhoto" x1="0" y1="0" x2="1" y2="1">
            <stop offset="0" stop-color="#8a3a30"/>
            <stop offset="0.45" stop-color="#5a221c"/>
            <stop offset="1" stop-color="#241311"/>
          </linearGradient>
        </defs>
        <path role="img" aria-label="Foto de cortes de carne vermelha crua com ervas, escurecida ao fundo"
              d="M0,350 C180,300 380,250 550,235 L550,880 L0,880 Z" fill="url(#meatPhoto)"/>
        <path d="M0,350 C180,300 380,250 550,235 L550,880 L0,880 Z" fill="rgba(20,14,13,0.35)"/>
        <path d="M0,342 C180,290 380,232 550,212 L550,235 C380,250 180,300 0,350 Z" fill="url(#goldBandLeft)"/>
      </svg>
      <div class="section-title">Sobre nossa empresa</div>
      <div class="about-text">
        <p>Lorem ipsum dolor sit amet, consectetur adipiscing elit. Phasellus iaculis bibendum auctor. Mauris tempus at nisi vitae lobortis.</p>
        <p>Sed commodo nec enim vitae vestibulum. Cras porta leo eget orci elementum tincidunt. Vivamus aliquam ligula non quam auctor, nec cursus neque sagittis. Vestibulum id varius nulla. Duis molestie libero quis nibh feugiat gravida. Aenean et neque a ligula luctus facilisis nec sit amet dui.</p>
        <p>Duis auctor arcu a dictum suscipit. Cras nisl odio, tempor eu neque id, sodales laoreet neque. Pellentesque pulvinar ligula eget enim porta, non porttitor tellus convallis. Sed eget elit ac quam elementum ornare ut nec risus. Pellentesque aliquet ultricies dolor, vitae viverra arcu ullamcorper eu. Pellentesque eu mi et sapien faucibus maximus et a mi.</p>
        <p>Cras vulputate nisi sit amet ante malesuada ultricies. Curabitur vulputate ultricies erat, a lacinia leo ultricies quis. Proin tincidunt, est nec tincidunt tempus, nibh tellus viverra quam, id tincidunt magna nisi sit amet nisl. Cras ex tortor, interdum id sollicitudin a, eleifend vitae neque. Integer id pharetra enim. Etiam mauris mauris, maximus facilisis arcu a, commodo convallis tellus. Ut mattis sit amet sem quis faucibus. Aliquam sed mauris velit.</p>
      </div>
      <div class="fold-shade"></div>
    </section>

    <section class="page page--products">
      <svg class="page-art" viewBox="0 0 550 880">
        <defs>
          <linearGradient id="goldBandRight" x1="0" y1="0" x2="1" y2="0">
            <stop offset="0" stop-color="#f4d27a"/>
            <stop offset="0.4" stop-color="#d9a431"/>
            <stop offset="1" stop-color="#9c6a12"/>
          </linearGradient>
          <linearGradient id="darkPanel" x1="0" y1="0" x2="1" y2="1">
            <stop offset="0" stop-color="#4a2420"/>
            <stop offset="0.5" stop-color="#2e2322"/>
            <stop offset="1" stop-color="#1c1817"/>
          </linearGradient>
        </defs>
        <path role="img" aria-label="Foto de carne vermelha em tom escuro ao fundo"
              d="M0,235 C150,215 350,195 550,190 L550,880 L0,880 Z" fill="url(#darkPanel)"/>
        <path d="M0,212 C150,194 350,178 550,174 L550,190 C350,195 150,215 0,235 Z" fill="url(#goldBandRight)"/>
      </svg>
      <div class="section-title">Nossos Produtos</div>
      <div class="product-grid">
        <div class="product">
          <div class="product-photo product-photo--lamb" role="img" aria-label="Foto de costela de cordeiro crua"></div>
          <div class="product-name">Cordeiros<br>linha Serra Lamb</div>
        </div>
        <div class="product">
          <div class="product-photo product-photo--beef" role="img" aria-label="Foto de bife bovino cru com pimenta"></div>
          <div class="product-name">Bovinos<br>linha Vale Nobre Beef</div>
        </div>
        <div class="product">
          <div class="product-photo product-photo--fish" role="img" aria-label="Foto de peixe fresco com limão"></div>
          <div class="product-name">Pescado<br>linha Mar Azul Fish</div>
        </div>
        <div class="product">
          <div class="product-photo product-photo--fries" role="img" aria-label="Foto de batatas fritas"></div>
          <div class="product-name">Batatas pre Pré-frita<br>linha Campo Fries</div>
        </div>
      </div>
      <div class="fold-shade"></div>
    </section>
  </div>
</body>
</html>
```